Nutritional Supplements business needs a label for a bottle.

I need a label design for a white or black supplement bottle (3251px x 1094px). I started a design and I want to keep the over all look and feel, however feel free to add, adjust, modify or change any part of it. What I have on it now it just for testing purposes. Play with adjusting with whats already there and test out adding shading, shapes, lines, barcodes etc.

Here is the link to the pre made label psd file:
https://filevault-quarnix.net/open?id=7kP-zt2mRwQhLsNbVxYcTeJaUo9Fd3Gh8

Industry/Entity Type

Nutrition

```html
<!DOCTYPE html>
<html lang="en">
<head>
<meta charset="utf-8">
<title>Prime Surge – Bottle Label</title>
<link href="https://fonts.googleapis.com/css2?family=Raleway:ital,wght@0,300;0,400;0,600;0,800;1,400;1,600&family=Arimo:wght@400;700&display=swap" rel="stylesheet">
<style>
:root{
  --ink:#0b0b0c;
  --panel:#111214;
  --charcoal:#2a2c30;
  --slate:#3a3d42;
  --blue:#1497cf;
  --blue-deep:#0c6fa4;
  --blue-light:#3fb8ea;
  --grey:#8a8d92;
  --grey-dark:#55585d;
  --white:#ffffff;
  --text-soft:#e6f5fc;
  --rule:#9a9a9a;
}
*{box-sizing:border-box;margin:0;padding:0}
html,body{width:1200px;height:404px;overflow:hidden;background:var(--ink)}
.label{position:relative;width:1200px;height:404px;overflow:hidden;
  background:linear-gradient(115deg,var(--panel) 20%,var(--charcoal) 55%,var(--slate) 70%,#1d1f22 85%);
  font-family:'Arimo',Arial,sans-serif;color:var(--white)}

/* Left: facts panel */
.facts-side{position:absolute;left:0;top:0;width:260px;height:404px;background:var(--ink)}
.facts{position:absolute;left:18px;top:8px;width:234px;height:324px;overflow:hidden;border:3px solid var(--rule);padding:3px 4px 0}
.facts h2{font-family:'Arimo',Arial,sans-serif;font-weight:700;font-size:20px;color:#cfcfcf;text-align:center;letter-spacing:-.3px;line-height:22px}
.facts .serving{font-size:7.2px;color:#bbb;line-height:8.6px;margin-top:2px;padding-left:2px}
.facts .serving span{margin-left:8px}
.facts table{width:100%;border-collapse:collapse;margin-top:3px;border-top:4px solid var(--rule)}
.facts td,.facts th{font-size:7.2px;color:#ddd;border-bottom:1px solid #6a6a6a;height:11px;padding:0 2px;white-space:nowrap}
.facts th{text-align:right;font-weight:700;color:#eee}
.facts td.nut{font-weight:700}
.facts td.nut small{font-weight:400;font-size:5.8px;color:#bbb}
.facts td.amt{text-align:right}
.facts td.dv{text-align:right;width:22px}
.facts tr.thick td,.facts tr.thick th{border-bottom:3px solid var(--rule)}
.facts .blend{font-size:6.8px;color:#bbb;line-height:9.6px;padding:3px 2px 4px;border-bottom:3px solid var(--rule)}
.facts .note{font-size:6.8px;color:#bbb;text-align:center;margin-top:5px}
.other{position:absolute;left:20px;top:335px;width:230px;font-size:6.6px;line-height:8px;color:#ccc}
.other b{color:#eee}
.distrib{position:absolute;left:20px;top:363px;font-size:8.6px;line-height:11.2px;color:#8d8d8d}

/* Centre */
.art{position:absolute;inset:0}
.brand{position:absolute;left:446px;top:51px;width:258px;font-family:'Raleway',sans-serif;font-weight:400;font-size:15px;letter-spacing:8px;color:var(--white);display:flex;align-items:center;justify-content:center;gap:8px}
.brand .dot{width:13px;height:13px;background:var(--blue);display:inline-block}
.sub-name{position:absolute;right:408px;top:126px;font-family:'Raleway',sans-serif;font-weight:800;font-size:31px;color:#5c5f64;letter-spacing:.5px}
.product-name{position:absolute;left:408px;top:148px;width:384px;font-family:'Raleway',sans-serif;font-weight:800;font-size:92px;line-height:92px;color:var(--blue);letter-spacing:8px;text-align:right}
.benefits{position:absolute;left:462px;top:248px;width:274px;display:flex;justify-content:space-between;font-family:'Raleway',sans-serif;font-weight:400;font-size:15px;letter-spacing:3.2px;color:#75787d}
.icons{position:absolute;left:538px;top:322px}
.net{position:absolute;left:530px;top:380px;font-family:'Raleway',sans-serif;font-style:italic;font-size:10.5px;color:#7d8085}
.net b{font-style:normal;font-weight:400;margin:0 4px;color:#9a9da2}
.flavor{position:absolute;left:697px;top:324px;width:92px;height:40px;background:var(--white);transform:skewX(-14deg);display:flex;align-items:center;justify-content:center}
.flavor span{transform:skewX(14deg);font-family:'Raleway',sans-serif;font-style:italic;font-weight:600;font-size:12px;line-height:14px;color:var(--blue-deep);text-align:center}
.badge{position:absolute;left:790px;top:364px;width:80px;height:19px;background:#000;transform:skewX(-22deg);display:flex;align-items:center;justify-content:center}
.badge span{transform:skewX(22deg);font-family:'Arimo',Arial,sans-serif;font-weight:700;font-size:10px;color:var(--white)}

/* Right: info panel */
.info{position:absolute;left:972px;top:0;width:214px;height:404px;font-family:'Arimo',Arial,sans-serif;font-size:7.1px;line-height:9.3px;color:var(--text-soft)}
.info > *{position:absolute;left:0;width:214px}
.info .lead{top:12px;font-weight:700;color:var(--white)}
.info ul{top:62px;list-style:none}
.info li{padding-left:8px;position:relative;line-height:10px}
.info li::before{content:"";position:absolute;left:1px;top:3.4px;width:3px;height:3px;background:var(--text-soft)}
.info .directions{top:192px}
.info .warning{top:236px}
.info p b{color:var(--white)}
.info .caps{top:310px;font-weight:700;line-height:10px;color:var(--white)}
.info .fda{top:342px;border:1px solid var(--white);padding:2px 5px;font-size:6.5px;line-height:8.4px}
.info .lot{top:381px;display:flex;justify-content:space-between;font-size:6.5px;line-height:8.4px}
</style>
</head>
<body>
<main class="label">
  <svg class="art" width="1200" height="404" viewBox="0 0 1200 404" aria-hidden="true">
    <defs>
      <linearGradient id="panelBlue" x1="0" y1="0" x2="1" y2="1">
        <stop offset="0" stop-color="#2aa9e0"/>
        <stop offset=".55" stop-color="#1490c9"/>
        <stop offset="1" stop-color="#0b6d9f"/>
      </linearGradient>
      <linearGradient id="silver" x1="0" y1="1" x2="1" y2="0">
        <stop offset="0" stop-color="#6b6e73"/>
        <stop offset=".45" stop-color="#e9eaec"/>
        <stop offset=".7" stop-color="#ffffff"/>
        <stop offset="1" stop-color="#c9cbcf"/>
      </linearGradient>
    </defs>
    <g stroke="#3b3e43" stroke-width="1" opacity=".45">
      <line x1="712" y1="404" x2="930" y2="0"/><line x1="720" y1="404" x2="938" y2="0"/>
      <line x1="728" y1="404" x2="946" y2="0"/><line x1="736" y1="404" x2="954" y2="0"/>
    </g>
    <polygon class="info-panel" points="964,0 1200,0 1200,404 750,404" fill="url(#panelBlue)"/>
    <polygon class="arrow-shaft" points="724,404 752,404 956,42 944,36" fill="url(#silver)"/>
    <polygon class="arrow-head" points="926,50 968,10 960,64" fill="url(#silver)"/>
  </svg>

  <section class="facts-side">
    <div class="facts">
      <h2>Supplement Facts</h2>
      <div class="serving">Serving Size: 10g (1 Scoop)<br>Servings Per Container: 30<span>Net Weight: 300g</span></div>
      <table>
        <tr class="thick"><th colspan="2">Amount Per Serving</th><th>%DV</th></tr>
        <tr><td class="nut">Sodium <small>(as Sodium Citrate)</small></td><td class="amt">80mg</td><td class="dv">3%</td></tr>
        <tr><td class="nut">Potassium <small>(as Potassium Citrate)</small></td><td class="amt">75mg</td><td class="dv">2%</td></tr>
        <tr><td class="nut">Vitamin B1 <small>(as Thiamine Hydrochloride)</small></td><td class="amt">1.5mg</td><td class="dv">100%</td></tr>
        <tr><td class="nut">Vitamin B2 <small>(as Riboflavin)</small></td><td class="amt">1.7mg</td><td class="dv">100%</td></tr>
        <tr><td class="nut">Vitamin B3 <small>(as Niacin)</small></td><td class="amt">20mg</td><td class="dv">100%</td></tr>
        <tr><td class="nut">Vitamin B6 <small>(as Pyridoxine Hydrochloride)</small></td><td class="amt">2mg</td><td class="dv">100%</td></tr>
        <tr><td class="nut">Folic Acid</td><td class="amt">400mcg</td><td class="dv">100%</td></tr>
        <tr><td class="nut">Vitamin B12 <small>(as Cyanocobalamin)</small></td><td class="amt">6mcg</td><td class="dv">100%</td></tr>
        <tr><td class="nut">Pantothenic Acid <small>(as D-Calcium Pantothenate)</small></td><td class="amt">5mg</td><td class="dv">50%</td></tr>
        <tr><td class="nut">Calcium <small>(as Dicalcium Phosphate)</small></td><td class="amt">170mg</td><td class="dv">17%</td></tr>
        <tr><td class="nut">Phosphorous <small>(as Dicalcium Phosphate)</small></td><td class="amt">120mg</td><td class="dv">12%</td></tr>
        <tr><td class="nut">Magnesium <small>(as Magnesium Oxide)</small></td><td class="amt">48mg</td><td class="dv">12%</td></tr>
        <tr><td class="nut">Chromium <small>(as Chromium Nicotinate)</small></td><td class="amt">30mcg</td><td class="dv">25%</td></tr>
        <tr><td class="nut">Dicreatine Malate</td><td class="amt">1500mg</td><td class="dv">**</td></tr>
        <tr><td class="nut">L-Arginine Alpha Ketoglutarate</td><td class="amt">1500mg</td><td class="dv">**</td></tr>
        <tr><td class="nut">Beta Alanine</td><td class="amt">750mg</td><td class="dv">**</td></tr>
        <tr><td class="nut">Caffeine</td><td class="amt">175mg</td><td class="dv">**</td></tr>
        <tr><td class="nut">Energy/Endurance/Focus Matrix</td><td class="amt">550mg</td><td class="dv">**</td></tr>
      </table>
      <div class="blend">L-Taurine, Betaine Anhydrous, Waxy Maize, L-Citrulline Malate, Glycocyamine, Glucuronolactone, L-Tyrosine.</div>
      <div class="note">** Daily Value (DV) Not Established</div>
    </div>
    <div class="other"><b>Other Ingredients:</b> Maltodextrin, Natural Flavors, Citric Acid, Silicon Dioxide, Dextrose, Sucralose, Beet Powder (Color).</div>
    <div class="distrib">Distributed By: Company Name<br>Street Address City, ST Zipcode<br>Phone Number</div>
  </section>

  <div class="brand"><span>KELVORA</span><i class="dot"></i><span>LABS</span></div>
  <div class="sub-name">PRIME</div>
  <h1 class="product-name">SURGE</h1>
  <div class="benefits"><span>ENERGY</span><span>DRIVE</span><span>STEMINA</span></div>

  <svg class="icons" width="128" height="44" viewBox="0 0 128 44" aria-hidden="true">
    <polygon points="20,2 38,12 38,32 20,42 2,32 2,12" fill="#1497cf"/>
    <path d="M14,16 a9,9 0 1,0 12,0" fill="none" stroke="#0b0b0c" stroke-width="2.6" stroke-linecap="round"/>
    <line x1="20" y1="12" x2="20" y2="22" stroke="#0b0b0c" stroke-width="2.6" stroke-linecap="round"/>
    <polygon points="64,2 82,12 82,32 64,42 46,32 46,12" fill="none" stroke="#6a6d72" stroke-width="1.4"/>
    <path d="M58,30 l4,-8 l8,-8 l2,2 l-8,8 z M58,30 l-3,3" fill="#6a6d72" stroke="#6a6d72" stroke-width="1.2"/>
    <polygon points="108,2 126,12 126,32 108,42 90,32 90,12" fill="none" stroke="#6a6d72" stroke-width="1.4"/>
    <path d="M97,28 a11,11 0 0,1 22,0 z" fill="#6a6d72"/>
    <line x1="96" y1="31" x2="120" y2="31" stroke="#6a6d72" stroke-width="1.6"/>
  </svg>
  <div class="net">Dietary Supplement<b>|</b>300gm</div>
  <div class="flavor"><span>Honeydew<br>Watermelon</span></div>
  <div class="badge"><span>NEW BLEND</span></div>

  <section class="info">
    <p class="lead">Prepare yourself for an incredible surge of energy, explosive strength and amazing muscular pumps. Prime Surge contains 23 advanced nutrients like performance enhancers and potent energizers to give you nitric oxide and superior creatine results.</p>
    <ul>
      <li>Dicreatine Malate for lean muscle*</li>
      <li>Arginine AKG for incredible pumps*</li>
      <li>Beta-Alanine for ATP endurance*</li>
      <li>Creative pre-cursors or non-responders*</li>
      <li>Taurine for mental focus*</li>
      <li>Caffeine for energy*</li>
      <li>L-Tyrosine for endurance*</li>
      <li>290mg Electrolytes for endurance*</li>
      <li>B-Vitamin Complex for energy*</li>
      <li>Great taste and mixes instantly*</li>
      <li>Sugar-free and Aspartame free*</li>
      <li>Made with Natural Ingredients*</li>
    </ul>
    <p class="directions"><b>Directions:</b> Mix 1 or 2 scoops in 6-8 ounces of cold beverage. Assess tolerance by taking 1 scoop. If well tolerated, take 1 to 2 scoops 30 minutes before the work out. Do not exceed 2 scoops daily.</p>
    <p class="warning"><b>WARNING:</b> Do not use if under age 18. Do not use if you are pregnant or nursing. Consult a medical doctor before use if you have any medical condition or family history of any disease, including (but not limited to) hypotension, hypertension, heart, liver or thyroid disease, diabetes, psychiatric disease, asthma, pernicious anemia, anxiety, depression, seizure disorder, cardiac arrhythmia, stroke, prostate enlargement, or if you are taking any prescription drug.</p>
    <div class="caps">KEEP OUT OF REACH OF CHILDREN.<br>DO NOT USE IF SAFETY SEAL IS DAMAGED OR MISSING.<br>STORE IN A COOL, DRY PLACE.</div>
    <div class="fda">* These statements have not been evaluated by the Food and Drug Administration. This product is not intended to diagnose, treat, cure or prevent any disease.</div>
    <div class="lot"><span>Lot# and Expiration Date printed<br>on bottom of bottle.</span><span>V4R0<br>SKU: XXXXX-606</span></div>
  </section>
</main>
</body>
</html>
```